Summer Fun

I need a Poster for Front of hotel advertising discounted drinks on Thursday & Fridays
$3.50.
Schooners of Local Beer, Glass of House Wine & Bubbly.
From 3.30pm to 6.30 pm
Nibblies Provided

Target Market(s)

25 + Market

Industry/Entity Type

Hotel

Requirements
Should not have
• Do not want to be known as Happy Hour.

```html
<!DOCTYPE html>
<html lang="en">
<head>
<meta charset="utf-8">
<title>Summer Fun</title>
<link href="https://fonts.googleapis.com/css2?family=Jost:wght@400&family=Oswald:wght@400&family=Norican&display=swap" rel="stylesheet">
<style>
  :root {
    --paper: #f8efe6;
    --photo-tone: #4a3728;
    --title-blue: #a9dbe9;
    --band-yellow: #f8c95c;
    --band-edge: #f4a05a;
    --price-orange: #f4a05a;
    --stripe-peach: #f7d2b0;
    --cream-text: #fbf1e4;
  }
  html, body {
    margin: 0;
    padding: 0;
    width: 849px;
    height: 1200px;
    overflow: hidden;
    background: var(--paper);
  }
  .poster {
    position: relative;
    width: 849px;
    height: 1200px;
    background: var(--paper);
  }
  .card {
    position: absolute;
    left: 26px;
    top: 30px;
    width: 802px;
    height: 1140px;
    border-radius: 30px;
    overflow: hidden;
  }
  .landscape-photo {
    position: absolute;
    inset: 0;
    background: var(--photo-tone);
  }
  .title {
    position: absolute;
    left: 0;
    right: 0;
    top: 322px;
    margin: 0;
    text-align: center;
    font-family: "Jost", sans-serif;
    font-weight: 400;
    font-size: 128px;
    letter-spacing: 4px;
    color: var(--title-blue);
    line-height: 1;
    white-space: nowrap;
  }
  .band {
    position: absolute;
    left: 0;
    right: 0;
    background: var(--band-yellow);
    border-top: 6px solid var(--band-edge);
    border-bottom: 6px solid var(--band-edge);
    box-sizing: border-box;
    display: flex;
    align-items: center;
    justify-content: center;
    text-align: center;
    font-family: "Norican", cursive;
    color: #ffffff;
  }
  .band--schedule {
    top: 448px;
    height: 132px;
    font-size: 30px;
    letter-spacing: 1.5px;
    word-spacing: 8px;
    white-space: nowrap;
  }
  .band--offer {
    top: 915px;
    height: 150px;
    font-size: 30px;
    line-height: 1.65;
    letter-spacing: 1.5px;
    word-spacing: 6px;
    padding: 0 40px;
  }
  .price-panel {
    position: absolute;
    left: 0;
    top: 580px;
    width: 802px;
    height: 335px;
    background: var(--paper);
  }
  .price-panel svg { display: block; }
  .price {
    position: absolute;
    left: 0;
    width: 812px;
    top: 58px;
    text-align: center;
    font-family: "Oswald", sans-serif;
    font-size: 112px;
    color: var(--cream-text);
    line-height: 1;
  }
</style>
</head>
<body>
<div class="poster">
  <div class="card">
    <div class="landscape-photo" role="img" aria-label="Photograph of a sunset over flat rural grassland with a lone tree"></div>

    <h1 class="title">Summer Fun</h1>

    <div class="band band--schedule">Thursdays &amp; Fridays from 330pm till 630pm</div>

    <div class="price-panel">
      <svg width="802" height="335" viewBox="0 0 802 335" aria-hidden="true">
        <g fill="var(--stripe-peach)" opacity="0.55">
          <rect x="0" y="12" width="802" height="38"/>
          <rect x="0" y="100" width="802" height="40"/>
          <rect x="0" y="188" width="802" height="40"/>
          <rect x="0" y="272" width="802" height="38"/>
        </g>
        <g fill="var(--stripe-peach)" opacity="0.35">
          <polygon points="0,50 120,50 300,240 0,240"/>
          <polygon points="802,50 690,50 510,240 802,240"/>
        </g>
        <polygon points="93,8 724,8 405,312" fill="var(--price-orange)" stroke="var(--title-blue)" stroke-width="6" stroke-linejoin="miter"/>
      </svg>
      <div class="price">$3.50</div>
    </div>

    <div class="band band--offer">Schooner of local beer, glass of house wine<br>or bubbly. Plus nibblies.</div>
  </div>
</div>
</body>
</html>
```